Harbor Petroleum Business Cards

I would like to design some options for about 10 sets of double sided business cards for our team with a raised logo with a Silver glossy finished logo. We are a privately funded upstream Oil & Gas producer drilling vertical wells in Central Oklahoma with a long term production (ROI driven) strategy that we implement through an annual drilling program. We are focused on a shallow / vertical / long life / low decline strategy. We are based in downtown Tulsa Oklahoma. I have attached a sample business card and a picture of our hallway logo which we would like to replicate on the business cards.

Target Market(s)

SEC Accredited Investors and other Oil & Gas Operators

Industry/Entity Type

Upstream Oil & Gas

Contact Information for Business Card

You can see the sample photo attached, but email / website / address / direct phone / Cell Phone / Name / Title / Fax

Font styles to use
Other font styles liked:
• Felix Titling

Colors
0054AA
0677BA
7BADD7
CADEEF
E8F1F8

Requirements
Must have
• Glossy raised logo
Nice to have
• Possibly a new logo.
Should not have
• No Greens /

```html
<!DOCTYPE html>
<html lang="en">
<head>
<meta charset="utf-8">
<title>Harbor Petroleum Business Cards</title>
<link href="https://fonts.googleapis.com/css2?family=Montserrat:wght@400;500;700&display=swap" rel="stylesheet">
<style>
  :root {
    --backdrop: #4a4a4a;
    --card: #141414;
    --silver: #d9d9d9;
    --silver-soft: #a9a9a9;
    --rule: #8a8a8a;
  }
  * { margin: 0; padding: 0; box-sizing: border-box; }
  html, body { width: 1200px; height: 801px; overflow: hidden; }
  body {
    background: var(--backdrop);
    font-family: "Montserrat", sans-serif;
    position: relative;
  }
  .card {
    position: absolute;
    top: 252px;
    width: 520px;
    height: 297px;
    background: var(--card);
    border-radius: 2px;
    box-shadow: 0 10px 24px rgba(0,0,0,0.35);
  }
  .card--contact { left: 50px; }
  .card--brand { left: 630px; }

  .contact-layout {
    position: absolute;
    top: 54px;
    right: 36px;
    display: flex;
    align-items: flex-start;
  }
  .identity {
    text-align: right;
    padding-right: 14px;
    padding-top: 58px;
  }
  .identity__name {
    font-weight: 700;
    font-size: 17px;
    color: var(--silver);
    letter-spacing: 0.3px;
  }
  .identity__title,
  .identity__dept {
    font-size: 13px;
    color: var(--silver-soft);
    margin-top: 3px;
  }
  .divider {
    width: 1px;
    height: 150px;
    background: var(--rule);
  }
  .details {
    padding-left: 14px;
    font-size: 12.5px;
    line-height: 19px;
    color: var(--silver);
  }
  .details__address { margin-bottom: 4px; color: var(--silver-soft); }
  .details__row { display: flex; align-items: center; gap: 7px; }
  .details__row svg { width: 11px; height: 11px; fill: var(--silver); flex: none; }

  .brand {
    position: absolute;
    inset: 0;
    display: flex;
    align-items: center;
    justify-content: center;
    gap: 14px;
  }
  .brand__dot {
    width: 22px;
    height: 22px;
    border-radius: 50%;
    background: var(--silver);
  }
  .brand__name {
    font-weight: 500;
    font-size: 28px;
    letter-spacing: 1.5px;
    color: var(--silver);
  }
</style>
</head>
<body>
  <section class="card card--contact">
    <div class="contact-layout">
      <div class="identity">
        <p class="identity__name">DORIAN K. WELLSTEAD, CPL</p>
        <p class="identity__title">Executive Vice President</p>
        <p class="identity__dept">Land, Legal &amp; Business Development</p>
      </div>
      <div class="divider"></div>
      <div class="details">
        <p class="details__address">42 East 3rd Street<br>Suite 900, Tulsa, OK 74103</p>
        <p class="details__row"><svg viewBox="0 0 12 12"><path d="M2.5 1h2l1 3-1.3 1a7 7 0 0 0 2.8 2.8l1-1.3 3 1v2c0 .8-.7 1.5-1.5 1.5A9.5 9.5 0 0 1 1 2.5C1 1.7 1.7 1 2.5 1z"/></svg>539-555-0142</p>
        <p class="details__row"><svg viewBox="0 0 12 12"><path d="M3 0h6a1 1 0 0 1 1 1v10a1 1 0 0 1-1 1H3a1 1 0 0 1-1-1V1a1 1 0 0 1 1-1zm0 1.5v7.5h6V1.5z"/></svg>918-555-0187</p>
        <p class="details__row"><svg viewBox="0 0 12 12"><path d="M3 0h5v3H3zM1 4h10v5H9v3H3V9H1zm3 5v2h4V9z"/></svg>918-555-0163</p>
        <p class="details__row"><svg viewBox="0 0 12 12"><path d="M0 2h12v1L6 7 0 3zm0 2.3L6 8l6-3.7V10H0z"/></svg>DKW@HPTulsa.com</p>
        <p class="details__row"><svg viewBox="0 0 12 12"><path d="M6 0a6 6 0 1 0 0 12A6 6 0 0 0 6 0zm0 1.5c.6 0 1.3 1.6 1.4 3.7H4.6C4.7 3.1 5.4 1.5 6 1.5zM4.6 6.8h2.8c-.1 2.1-.8 3.7-1.4 3.7s-1.3-1.6-1.4-3.7z"/></svg>www.HarborPetroleumLLC.com</p>
      </div>
    </div>
  </section>

  <section class="card card--brand">
    <div class="brand">
      <span class="brand__dot"></span>
      <span class="brand__name">HARBOR PETROLEUM, LLC</span>
    </div>
  </section>
</body>
</html>
```